Business Card Design

Cake decorating business in a small town in Australia. looking for a style that is fresh with a touch of vintage/country. liking these ideas, timber backgrounds, chalkboards, bunting, flowers and cake elements (rolling pins, cupcakes, cake stands, etc.) would consider a shot saying/statement. would like the back of the card to have wording "Specialising in delectable treats for all your special occasions" - wedding cakes - birthday cakes - special occasion cakes - novelty cakes - cupcakes, cookies, slices and cake pops. maybe incorporate a cake in design on back page. attached are a few of my favourite cakes and the start of a card design I liked.

Industry/Entity Type

Business

Contact Information for Business Card

Marla's Sugarcrest Kitchen 0438 056 969Find me on (Friendbook Logo)

Requirements
Nice to have
• timber, some of my designs, chalkboard, baking utensils
Should not have
• no red font

```html
<!DOCTYPE html>
<html lang="en">
<head>
<meta charset="utf-8">
<title>Marla's Sugarcrest Kitchen – Business Card</title>
<link rel="stylesheet" href="https://fonts.googleapis.com/css2?family=Open+Sans:ital,wght@0,400;0,600;0,700;1,400&display=swap">
<style>
  :root {
    --page: #d9d9d9;
    --card-edge: #080808;
    --card-mid: #202020;
    --ink: #ffffff;
    --ink-soft: #ececec;
    --rule: #303030;
    --stand-light: #f4f4f4;
    --stand-dark: #9a9a9a;
    --dot: #2f5fa8;
  }
  * { box-sizing: border-box; margin: 0; padding: 0; }
  html, body {
    width: 1200px; height: 900px; overflow: hidden;
    background: var(--page);
    font-family: "Open Sans", sans-serif;
  }
  .sheet {
    width: 1200px; height: 900px;
    display: flex; flex-direction: column; align-items: center; justify-content: center;
    gap: 36px;
  }
  .card {
    position: relative;
    width: 640px; height: 391px;
    background: radial-gradient(ellipse at 50% 35%, var(--card-mid) 0%, var(--card-edge) 85%);
    color: var(--ink);
    box-shadow: 0 4px 14px rgba(0,0,0,0.25);
    overflow: hidden;
  }
  .brand-name {
    font-weight: 600; color: var(--ink);
    text-align: center; line-height: 1.2;
  }

  /* Front */
  .card--front .phone {
    position: absolute; left: 52px; top: 120px;
    display: flex; align-items: center; gap: 14px;
    font-size: 17px; font-style: italic; letter-spacing: 0.6px;
  }
  .card--front .phone svg { width: 12px; height: 12px; fill: var(--ink); }
  .card--front .divider {
    position: absolute; left: 200px; right: 70px; top: 196px;
    height: 1px; background: var(--rule);
  }
  .card--front .brand {
    position: absolute; right: 40px; top: 56px; width: 220px;
    display: flex; flex-direction: column; align-items: center; gap: 14px;
  }
  .card--front .brand-name { font-size: 18px; }
  .card--front .cake-stand {
    width: 84px; height: 58px;
    border-radius: 50% 50% 12px 12px / 30% 30% 12px 12px;
    background: radial-gradient(ellipse at 50% 30%, var(--stand-light) 0%, var(--stand-dark) 70%, transparent 100%);
  }
  .card--front .social {
    position: absolute; right: 40px; bottom: 42px;
    display: flex; align-items: center; gap: 12px;
    font-size: 20px; font-weight: 600;
  }
  .card--front .social .dot {
    width: 34px; height: 34px; border-radius: 50%; background: var(--dot);
  }

  /* Back */
  .card--back .brand-name { margin-top: 52px; font-size: 19px; }
  .card--back .tagline {
    margin: 30px auto 0; width: 440px;
    text-align: center; font-weight: 700; font-size: 21px; line-height: 1.15;
  }
  .card--back .services {
    margin: 16px auto 0; width: 560px;
    list-style: none; text-align: center;
    font-size: 16px; line-height: 1.4; color: var(--ink-soft);
  }
  .card--back .services .sep {
    display: inline-block; width: 8px; height: 8px; border-radius: 50%;
    background: var(--ink); margin: 0 14px; vertical-align: middle;
  }
</style>
</head>
<body>
<main class="sheet">
  <section class="card card--front" aria-label="Card front">
    <div class="phone">
      <svg viewBox="0 0 24 24" aria-hidden="true"><path d="M6.6 10.8a15 15 0 0 0 6.6 6.6l2.2-2.2c.3-.3.7-.4 1-.2 1.1.4 2.3.6 3.6.6.6 0 1 .4 1 1V20c0 .6-.4 1-1 1A17 17 0 0 1 3 4c0-.6.4-1 1-1h3.5c.6 0 1 .4 1 1 0 1.3.2 2.5.6 3.6.1.3 0 .7-.2 1z"/></svg>
      <span>0471 283 514</span>
    </div>
    <div class="divider"></div>
    <div class="brand">
      <p class="brand-name">Marla's Sugarcrest<br>Kitchen</p>
      <div class="cake-stand" role="img" aria-label="Illustration of a white cake stand"></div>
    </div>
    <div class="social">
      <span>Find me on Friendbook</span>
      <span class="dot" aria-hidden="true"></span>
    </div>
  </section>

  <section class="card card--back" aria-label="Card back">
    <p class="brand-name">Marla's Sugarcrest Kitchen</p>
    <p class="tagline">Specialising in delectable treats for all your special occasions</p>
    <ul class="services">
      <li>Wedding Cakes<span class="sep"></span>Birthday cakes<span class="sep"></span>Special occasion cakes</li>
      <li>Novelty cakes<span class="sep"></span>Cupcakes<span class="sep"></span>Cookies</li>
      <li>Slices and Cake pops</li>
    </ul>
  </section>
</main>
</body>
</html>
```